BROCHURE

Hi. I am looking for a really professional design for this - it is an information pack for potential new agents/re-sellers for our company. pdf attached + images, feel free to experiment, use other images or if you think it requires editing to the text let me know. You will also find attached a brochure from another tuning company which you can use for ideas. thank you
automotive sector, car garage owners etc who may want an add on business, or those looking to get into vehicle tuning
It Company

```html
<!DOCTYPE html>
<html lang="en">
<head>
<meta charset="utf-8">
<title>Tuning Agent Information Pack</title>
<link href="https://fonts.googleapis.com/css2?family=Montserrat:wght@500;600;700&family=Open+Sans:wght@400;700&display=swap" rel="stylesheet">
<style>
  :root {
    --page-bg: #e4e6e7;
    --plate-light: #d9dadb;
    --plate-mid: #9c9fa1;
    --plate-dark: #5d6063;
    --panel-blue: #2ba4da;
    --frame-white: #ffffff;
    --header-dark: #2f2a29;
    --step-label: #6e7173;
    --step-bar: #c6cacb;
    --text-white: #ffffff;
  }
  * { margin: 0; padding: 0; box-sizing: border-box; }
  html, body { width: 1200px; height: 1200px; overflow: hidden; }
  body { background: var(--page-bg); position: relative; }

  .brochure {
    position: absolute;
    left: 190px; top: 20px;
    width: 820px; height: 1160px;
  }
  .metal-border {
    position: absolute; inset: 0;
    background:
      radial-gradient(ellipse at 30% 20%, rgba(255,255,255,0.55), transparent 55%),
      radial-gradient(ellipse at 75% 85%, rgba(255,255,255,0.4), transparent 50%),
      linear-gradient(135deg, var(--plate-dark), var(--plate-mid) 30%, var(--plate-light) 50%, var(--plate-mid) 70%, var(--plate-dark));
  }
  .info-panel {
    position: absolute;
    left: 45px; top: 45px;
    width: 730px; height: 1069px;
    background: var(--panel-blue);
    border: 4px solid var(--frame-white);
  }
  .headline {
    position: absolute;
    left: 45px; top: 45px;
    width: 632px; height: 116px;
    background: var(--header-dark);
    color: var(--text-white);
    font-family: "Montserrat", sans-serif;
    font-weight: 500;
    font-size: 23px;
    line-height: 30px;
    letter-spacing: 0.5px;
    text-align: center;
    display: flex; align-items: center; justify-content: center;
  }
  .steps {
    position: absolute;
    left: 45px; top: 185px;
    width: 632px;
    list-style: none;
  }
  .step {
    display: flex;
    height: 71px;
    margin-bottom: 7px;
  }
  .step-label {
    width: 70px;
    background: var(--step-label);
    color: var(--text-white);
    font-family: "Montserrat", sans-serif;
    font-weight: 700;
    font-size: 17px;
    line-height: 24px;
    letter-spacing: 0.5px;
    text-align: center;
    display: flex; flex-direction: column; justify-content: center;
  }
  .step-text {
    flex: 1;
    background: var(--step-bar);
    color: var(--text-white);
    font-family: "Montserrat", sans-serif;
    font-weight: 600;
    font-size: 18.5px;
    letter-spacing: 0.8px;
    padding-left: 20px;
    display: flex; align-items: center;
  }
  .details {
    position: absolute;
    left: 45px; top: 672px;
    width: 632px;
    color: var(--text-white);
    font-family: "Open Sans", sans-serif;
    font-size: 16px;
    line-height: 19.8px;
    letter-spacing: -0.4px;
    text-align: justify;
  }
  .details strong { font-weight: 700; }
</style>
</head>
<body>
  <div class="brochure">
    <div class="metal-border" role="img" aria-label="Brushed steel diamond tread plate border"></div>
    <section class="info-panel">
      <h1 class="headline">NO EXPERIENCE WITH TUNING?<br>DONT WORRY, YOUR JOB IS VERY EASY,<br>AND WE HANDLE THE HARD PART.</h1>
      <ol class="steps">
        <li class="step"><span class="step-label">STEP<span>1</span></span><span class="step-text">PLUG INTO OBD PORT ON VEHICLE</span></li>
        <li class="step"><span class="step-label">STEP<span>2</span></span><span class="step-text">READ ECU FILE (usually less than 5 mins)</span></li>
        <li class="step"><span class="step-label">STEP<span>3</span></span><span class="step-text">SEND US THE ECU FILE FOR TUNING</span></li>
        <li class="step"><span class="step-label">STEP<span>4</span></span><span class="step-text">RECEIVE MODIFIED FILE (LESS THAN 30 MINUTES)</span></li>
        <li class="step"><span class="step-label">STEP<span>5</span></span><span class="step-text">WRITE IN MODIFIED FILE (usually less than 5 mins)</span></li>
        <li class="step"><span class="step-label">STEP<span>6</span></span><span class="step-text">DRIVE VEHICLE</span></li>
      </ol>
      <div class="details">
        <p>Every time you tune a vehicle, the whole process including the test drive should take under an hour. While we tune your customers vehicle, you can continue about your work and we will notify you when the new software is ready.</p>
        <p>This way, tuning is a hassle free service that you can add to your business without the need for any previous tuning experience, with great profit margins and very little time consumption.</p>
        <p>Every vehicle tune is backed up with a <strong>30 day no quibble money back guarantee</strong>, so if you or your customers are not 100% satisfied, we will issue an instant refund and return the vehicle to original. Each vehicle is custom tuned to your customers requirements. Some customers want power, some want economy or maybe a blend of both.</p>
        <p>Other requests such as DTC error codes, Velta hot start issues, EGR &amp; DPF issues + more can be solved for most vehicles also.</p>
      </div>
    </section>
  </div>
</body>
</html>
```